Powerpoint deck to compliment logo

We have and like our logo. We need a standard PowerPoint deck to use in our many and varied presentations. We are happy with how we format them, but we need a template that compliments our logo. We are about health, wellness and safety in schools. We don't want a 'theme' which is too angular, but we do want color blocks, occasionally, within the templates. The deck should compliment our existing logo.

Target Market(s)

Employees

Industry/Entity Type

Healthcare, education and safety

Font styles to use
Serif
Other font styles liked:
• Century Schoolbook

Colors

Designer to choose colors to be used in the design.

Requirements
Must have
• colors which compliment our logo.
Nice to have
• Fluid objects
Should not have
• Angles

```html
<!DOCTYPE html>
<html lang="en">
<head>
<meta charset="utf-8">
<title>Ridgeway Schools Wellness Trust – Presentation Template</title>
<link href="https://fonts.googleapis.com/css2?family=Arimo:wght@400;700&display=swap" rel="stylesheet">
<style>
:root{
  --stage:#c9c9c9;
  --paper:#ffffff;
  --navy:#1f3f8f;
  --blue:#2f55a4;
  --slate:#5b78a9;
  --sky:#63b3e6;
  --green:#2e8b45;
  --lime:#7cc242;
  --mint:#cfe9c9;
  --ice:#d8e3f2;
  --ink:#4a4a4a;
  --photo-a:#b9a99a;
  --photo-b:#8fb6d9;
}
*{margin:0;padding:0;box-sizing:border-box}
html,body{width:1200px;height:660px;overflow:hidden;background:var(--stage);font-family:"Arimo",Arial,sans-serif}
.canvas{position:relative;width:1200px;height:660px}
.slide{position:absolute;width:195px;height:110px;background:var(--paper);overflow:hidden}
.slide *{position:absolute}
.slide b,.slide br{position:static}
.title{left:0;right:0;top:5px;text-align:center;font-size:8.5px;color:var(--blue)}
.copy{font-size:2.6px;line-height:1.35;color:var(--ink)}
.copy b{color:var(--navy)}
.copy.wide{left:14px;right:14px}
.footer{left:0;right:0;bottom:0;height:6px;background:linear-gradient(90deg,var(--slate),var(--green));color:#fff;font-size:2.8px;line-height:6px;padding-left:14px;font-weight:700}
.photo{background:linear-gradient(135deg,var(--photo-a),#e6ddd3)}
.photo.sky{background:linear-gradient(160deg,var(--photo-b),#e8e2d6)}
.dot{border-radius:50%}
.bold{font-weight:700}
.num{font-size:6px;font-weight:700}
.pill{height:6px;border-radius:3px;color:#fff;font-size:2.6px;line-height:6px;padding-left:5px;font-weight:700}
.chev{height:8px;color:#fff;font-size:2.8px;line-height:8px;text-align:center;clip-path:polygon(0 0,88% 0,100% 50%,88% 100%,0 100%,12% 50%)}
.para{height:9px;color:#fff;font-size:2.4px;line-height:1.3;padding:1.5px 5px;transform:skewX(-18deg)}
.box-label{color:#fff;text-align:center}
.box-label b{color:#fff}
</style>
</head>
<body>
<div class="canvas">

<!-- Row 1 -->
<section class="slide cover" style="left:83px;top:87px">
  <div style="left:0;top:0;width:195px;height:110px;background:var(--navy)"></div>
  <div class="dot" style="left:92px;top:-40px;width:190px;height:190px;background:var(--paper)"></div>
  <div style="left:12px;top:36px;color:#fff;font-size:9px;line-height:1.15">Lorem<br>Ipsum</div>
  <div style="left:12px;top:61px;width:70px;color:#fff;font-size:3px;line-height:1.3;font-weight:700">Lorem ipsum dolor sit amet, consectetuer adipiscing elit, sed diam nonummy</div>
  <div class="dot" style="left:126px;top:34px;width:14px;height:14px;background:var(--green)"></div>
  <div style="left:120px;top:52px;width:66px;color:var(--navy);font-size:6px;line-height:1.2;text-align:center">Ridgeway Schools<br>Wellness Trust</div>
</section>

<section class="slide agenda" style="left:293px;top:87px">
  <div class="title">Agenda</div>
  <div class="photo" role="img" aria-label="Photo of a tired person holding their head" style="left:0;top:22px;width:62px;height:72px"></div>
  <div class="num" style="left:70px;top:28px;color:var(--green)">01</div><div class="bold" style="left:86px;top:29px;font-size:4.5px;color:var(--green)">SubTitle</div>
  <div class="num" style="left:70px;top:48px;color:var(--lime)">02</div><div class="bold" style="left:86px;top:49px;font-size:4.5px;color:var(--lime)">SubTitle</div>
  <div class="num" style="left:70px;top:68px;color:var(--navy)">03</div><div class="bold" style="left:86px;top:69px;font-size:4.5px;color:var(--navy)">SubTitle</div>
  <div class="num" style="left:70px;top:88px;color:var(--slate)">04</div><div class="bold" style="left:86px;top:89px;font-size:4.5px;color:var(--slate)">SubTitle</div>
  <div class="copy" style="left:126px;top:29px;width:56px">• Lorem ipsum dolor sit amet<br>• Duis autem vel in hendrerit</div>
  <div class="copy" style="left:126px;top:49px;width:56px">• Lorem ipsum dolor sit amet<br>• Duis autem vel in hendrerit</div>
  <div class="copy" style="left:126px;top:69px;width:56px">• Lorem ipsum dolor sit amet<br>• Duis autem vel in hendrerit</div>
  <div class="copy" style="left:126px;top:88px;width:56px">• Lorem ipsum dolor sit amet<br>• Duis autem vel in hendrerit</div>
  <div class="footer">Ridgeway Schools Wellness Trust. All rights reserved.</div>
</section>

<section class="slide timeline-bar" style="left:503px;top:87px">
  <div class="title">Timeline</div>
  <div class="copy" style="left:18px;top:17px;width:160px">Lorem ipsum dolor sit amet, consectetuer adipiscing elit, sed diam nonummy nibh euismod tincidunt ut laoreet dolore magna aliquam erat volutpat. Ut wisi enim ad minim.</div>
  <div class="copy" style="left:40px;top:29px">• Lorem ipsum<br>• Lorem ipsum<br>• Lorem ipsum<br>• Lorem ipsum<br>• Lorem ipsum</div>
  <div class="copy" style="left:100px;top:29px">• Lorem ipsum<br>• Lorem ipsum<br>• Lorem ipsum<br>• Lorem ipsum<br>• Lorem ipsum</div>
  <div class="copy" style="left:158px;top:29px">• Lorem ipsum<br>• Lorem ipsum<br>• Lorem ipsum</div>
  <div class="chev" style="left:14px;top:60px;width:36px;background:#8fb0d8">2020</div>
  <div class="chev" style="left:47px;top:60px;width:36px;background:var(--slate)">2021</div>
  <div class="chev" style="left:80px;top:60px;width:36px;background:var(--navy)">2022</div>
  <div class="chev" style="left:113px;top:60px;width:36px;background:var(--lime)">2023</div>
  <div class="chev" style="left:146px;top:60px;width:36px;background:var(--green)">2024</div>
  <div class="copy" style="left:20px;top:73px">• Lorem ipsum<br>• Lorem ipsum<br>• Lorem ipsum<br>• Lorem ipsum</div>
  <div class="copy" style="left:80px;top:73px">• Lorem ipsum<br>• Lorem ipsum<br>• Lorem ipsum</div>
  <div class="copy" style="left:140px;top:73px">• Lorem ipsum<br>• Lorem ipsum<br>• Lorem ipsum<br>• Lorem ipsum</div>
  <div class="footer">Ridgeway Schools Wellness Trust. All rights reserved.</div>
</section>

<section class="slide timeline-wave" style="left:713px;top:87px">
  <div class="title">Timeline</div>
  <svg style="left:0;top:40px" width="195" height="40" viewBox="0 0 195 40">
    <path d="M20 30 Q20 12 35 12 Q50 12 50 22 Q50 32 62 32 Q74 32 74 22 Q74 12 88 12 Q102 12 102 22 Q102 32 114 32 Q126 32 126 22 Q126 12 140 12 Q154 12 154 22 Q154 32 166 32 Q178 32 178 20 Q178 12 195 12" fill="none" stroke="var(--green)" stroke-width="5"/>
    <path d="M74 22 Q74 12 88 12 Q102 12 102 22" fill="none" stroke="var(--navy)" stroke-width="5"/>
    <path d="M126 22 Q126 12 140 12 Q154 12 154 22" fill="none" stroke="var(--sky)" stroke-width="5"/>
    <path d="M166 32 Q178 32 178 20 Q178 12 195 12" fill="none" stroke="#c8c8c8" stroke-width="5"/>
    <circle cx="35" cy="22" r="4" fill="var(--green)"/><circle cx="62" cy="22" r="4" fill="var(--sky)"/>
    <circle cx="88" cy="22" r="4" fill="var(--slate)"/><circle cx="114" cy="22" r="4" fill="var(--lime)"/>
    <circle cx="140" cy="22" r="4" fill="var(--sky)"/><circle cx="166" cy="22" r="4" fill="var(--slate)"/>
  </svg>
  <div class="copy" style="left:40px;top:31px;width:30px;text-align:center">Lorem ipsum<br>Ut wisi enim ad</div>
  <div class="copy" style="left:96px;top:31px;width:30px;text-align:center">Lorem ipsum<br>Ut wisi enim ad</div>
  <div class="copy" style="left:150px;top:31px;width:30px;text-align:center">Lorem ipsum<br>Ut wisi enim ad</div>
  <div class="copy" style="left:10px;top:80px;width:34px;text-align:center">Lorem ipsum<br>Ut wisi enim ad</div>
  <div class="copy" style="left:66px;top:80px;width:34px;text-align:center">Lorem ipsum<br>Ut wisi enim ad</div>
  <div class="copy" style="left:122px;top:80px;width:34px;text-align:center">Lorem ipsum<br>Ut wisi enim ad</div>
  <div class="footer">Ridgeway Schools Wellness Trust. All rights reserved.</div>
</section>

<section class="slide icon-row" style="left:923px;top:87px">
  <div class="title">Lorem Ipsum</div>
  <div class="dot" style="left:13px;top:30px;width:6px;height:6px;background:var(--sky)"></div>
  <div style="left:22px;top:30px;font-size:4px;color:var(--navy)">Lorem Ipsum</div>
  <div class="dot" style="left:25px;top:42px;width:9px;height:9px;background:var(--green)"></div>
  <div class="dot" style="left:70px;top:42px;width:9px;height:9px;background:var(--lime)"></div>
  <div class="dot" style="left:115px;top:42px;width:9px;height:9px;background:var(--navy)"></div>
  <div class="dot" style="left:160px;top:42px;width:9px;height:9px;background:var(--slate)"></div>
  <div class="copy" style="left:12px;top:54px;width:36px;text-align:center"><b>Lorem Ipsum</b><br>Lorem ipsum dolor sit amet adipiscing elit</div>
  <div class="copy" style="left:57px;top:54px;width:36px;text-align:center"><b>Lorem Ipsum</b><br>Lorem ipsum dolor sit amet adipiscing elit</div>
  <div class="copy" style="left:102px;top:54px;width:36px;text-align:center"><b>Lorem Ipsum</b><br>Lorem ipsum dolor sit amet adipiscing elit</div>
  <div class="copy" style="left:147px;top:54px;width:36px;text-align:center"><b>Lorem Ipsum</b><br>Lorem ipsum dolor sit amet adipiscing elit</div>
  <div class="copy wide" style="top:76px">Lorem ipsum dolor sit amet, consectetuer adipiscing elit, sed diam nonummy nibh euismod tincidunt ut laoreet dolore magna aliquam erat volutpat ut wisi enim ad minim veniam.</div>
  <div class="footer">Ridgeway Schools Wellness Trust. All rights reserved.</div>
</section>

<!-- Row 2 -->
<section class="slide sub-topic" style="left:83px;top:212px">
  <div class="photo" role="img" aria-label="Photo of a hand holding a pill and a glass of water" style="left:0;top:0;width:100px;height:104px"></div>
  <div style="left:112px;top:20px;font-size:3px;color:var(--green)">Lorem Ipsum</div>
  <div class="bold" style="left:112px;top:30px;font-size:8px;color:var(--blue)">Sub Topic</div>
  <div class="copy" style="left:112px;top:50px;width:70px">Lorem ipsum dolor sit amet, consectetuer adipiscing elit sed diam nonummy nibh euismod tincidunt ut laoreet dolore magna aliquam erat volutpat ut wisi enim.</div>
  <div style="left:112px;top:88px;width:22px;height:5px;background:var(--green);color:#fff;font-size:2.5px;line-height:5px;text-align:center">Lorem</div>
  <div class="footer">Ridgeway Schools Wellness Trust. All rights reserved.</div>
</section>

<section class="slide text-photo" style="left:293px;top:212px">
  <div class="title">Lorem ipsum</div>
  <div style="left:14px;top:28px;width:80px;font-size:5px;color:var(--navy)">Lorem ipsum dolor sit amet</div>
  <div class="copy" style="left:14px;top:40px;width:80px;color:var(--green)">Lorem ipsum dolor sit amet consectetuer adipiscing elit</div>
  <div class="copy" style="left:14px;top:48px;width:80px">Lorem ipsum dolor sit amet, consectetuer adipiscing elit, sed diam nonummy nibh euismod tincidunt ut laoreet dolore magna aliquam erat volutpat. Ut wisi enim ad minim veniam quis nostrud.<br><br>Duis autem vel eum iriure dolor in hendrerit in vulputate velit esse molestie consequat.</div>
  <div class="photo sky" role="img" aria-label="Photo of a person doing a yoga pose on a beach" style="left:106px;top:24px;width:78px;height:64px"></div>
  <div class="footer">Ridgeway Schools Wellness Trust. All rights reserved.</div>
</section>

<section class="slide pills" style="left:503px;top:212px">
  <div class="title">Lorem ipsum</div>
  <div class="pill" style="left:30px;top:26px;width:46px;background:var(--green)">Your Text Here</div>
  <div class="pill" style="left:118px;top:26px;width:46px;background:var(--lime)">Your Text Here</div>
  <div class="pill" style="left:30px;top:64px;width:46px;background:var(--slate)">Your Text Here</div>
  <div class="pill" style="left:118px;top:64px;width:46px;background:var(--navy)">Your Text Here</div>
  <div class="dot" style="left:82px;top:24px;width:9px;height:9px;background:var(--green)"></div>
  <div class="dot" style="left:104px;top:24px;width:9px;height:9px;background:var(--lime)"></div>
  <div class="dot" style="left:82px;top:62px;width:9px;height:9px;background:var(--slate)"></div>
  <div class="dot" style="left:104px;top:62px;width:9px;height:9px;background:var(--navy)"></div>
  <div class="copy" style="left:30px;top:34px;width:46px;text-align:right">Lorem ipsum dolor sit amet, consectetuer adipiscing elit, sed diam nonummy nibh euismod tincidunt ut laoreet.</div>
  <div class="copy" style="left:118px;top:34px;width:46px">Lorem ipsum dolor sit amet, consectetuer adipiscing elit, sed diam nonummy nibh euismod tincidunt ut laoreet.</div>
  <div class="copy" style="left:30px;top:72px;width:46px;text-align:right">Lorem ipsum dolor sit amet, consectetuer adipiscing elit, sed diam nonummy nibh euismod tincidunt ut laoreet.</div>
  <div class="copy" style="left:118px;top:72px;width:46px">Lorem ipsum dolor sit amet, consectetuer adipiscing elit, sed diam nonummy nibh euismod tincidunt ut laoreet.</div>
  <div class="footer">Ridgeway Schools Wellness Trust. All rights reserved.</div>
</section>

<section class="slide icon-list" style="left:713px;top:212px">
  <div style="left:14px;top:18px;font-size:3px;color:var(--sky)">Lorem Ipsum</div>
  <div style="left:14px;top:25px;width:80px;font-size:6px;line-height:1.2;color:var(--navy)">Ut wisi enim ad minim veniam, quis nostrud</div>
  <div class="copy" style="left:14px;top:52px;width:75px">Lorem ipsum dolor sit amet, consectetuer adipiscing elit, sed diam nonummy nibh euismod tincidunt ut laoreet dolore magna aliquam erat volutpat. Ut wisi enim ad minim veniam.</div>
  <div style="left:114px;top:20px;width:5px;height:5px;background:var(--sky)"></div><div class="copy" style="left:124px;top:19px;width:58px"><b>Lorem ipsum</b><br>Lorem ipsum dolor sit amet elit</div>
  <div style="left:114px;top:35px;width:5px;height:5px;background:var(--slate)"></div><div class="copy" style="left:124px;top:34px;width:58px"><b>Lorem ipsum</b><br>Lorem ipsum dolor sit amet elit</div>
  <div style="left:114px;top:50px;width:5px;height:5px;background:var(--sky)"></div><div class="copy" style="left:124px;top:49px;width:58px"><b>Lorem ipsum</b><br>Lorem ipsum dolor sit amet elit</div>
  <div style="left:114px;top:65px;width:5px;height:5px;background:var(--slate)"></div><div class="copy" style="left:124px;top:64px;width:58px"><b>Lorem ipsum</b><br>Lorem ipsum dolor sit amet elit</div>
  <div style="left:114px;top:80px;width:5px;height:5px;background:var(--green)"></div><div class="copy" style="left:124px;top:79px;width:58px"><b>Lorem ipsum</b><br>Lorem ipsum dolor sit amet elit</div>
  <div class="footer">Ridgeway Schools Wellness Trust. All rights reserved.</div>
</section>

<section class="slide process" style="left:923px;top:212px">
  <div class="title">Lorem Ipsum</div>
  <div class="dot" style="left:13px;top:30px;width:6px;height:6px;background:var(--sky)"></div>
  <div style="left:22px;top:30px;font-size:4px;color:var(--navy)">Lorem Ipsum</div>
  <div class="chev" style="left:12px;top:42px;width:48px;height:11px;line-height:3.5px;padding-top:2px;background:var(--green);clip-path:polygon(0 0,85% 0,100% 50%,85% 100%,0 100%)">Lorem Ipsum<br>dolor sit amet</div>
  <div class="chev" style="left:55px;top:42px;width:48px;height:11px;line-height:3.5px;padding-top:2px;background:var(--lime)">Lorem Ipsum<br>dolor sit amet</div>
  <div class="chev" style="left:98px;top:42px;width:48px;height:11px;line-height:3.5px;padding-top:2px;background:var(--navy)">Lorem Ipsum<br>dolor sit amet</div>
  <div class="chev" style="left:141px;top:42px;width:44px;height:11px;line-height:3.5px;padding-top:2px;background:var(--slate)">Lorem Ipsum<br>dolor sit amet</div>
  <div class="copy wide" style="top:60px">Lorem ipsum dolor sit amet, consectetuer adipiscing elit, sed diam nonummy nibh euismod tincidunt ut laoreet dolore magna aliquam erat volutpat ut wisi enim ad minim veniam, quis nostrud exerci tation.</div>
  <div class="footer">Ridgeway Schools Wellness Trust. All rights reserved.</div>
</section>

<!-- Row 3 -->
<section class="slide sub-topic-alt" style="left:83px;top:333px">
  <div class="bold" style="left:12px;top:12px;font-size:7.5px;line-height:1.15;color:var(--sky)">Sub Topic<br>Slide</div>
  <div style="left:12px;top:36px;width:70px;font-size:4.5px;line-height:1.2;color:var(--navy)">Lorem ipsum dolor sit amet</div>
  <div class="copy" style="left:12px;top:50px;width:70px">Lorem ipsum dolor sit amet, consectetuer adipiscing elit</div>
  <div class="copy" style="left:12px;top:62px;width:70px"><b>Duis autem vel eum iriure dolor in hendrerit in vulputate velit esse</b></div>
  <div class="copy" style="left:12px;top:80px;width:70px">Lorem ipsum dolor sit amet, consectetuer adipiscing elit sed diam</div>
  <div class="photo sky" role="img" aria-label="Photo of a woman raising her arms at sunrise" style="left:98px;top:22px;width:97px;height:74px"></div>
  <div class="footer">Ridgeway Schools Wellness Trust. All rights reserved.</div>
</section>

<section class="slide steps" style="left:293px;top:333px">
  <div class="title">Lorem ipsum</div>
  <div class="bold" style="left:14px;top:28px;font-size:5.5px;color:var(--navy)">Lorem ipsum</div>
  <div class="copy" style="left:14px;top:37px;width:110px">Lorem ipsum dolor sit amet, consectetuer adipiscing elit, sed diam nonummy nibh euismod tincidunt ut laoreet dolore magna.</div>
  <div class="dot" style="left:14px;top:56px;width:8px;height:8px;background:var(--green);color:#fff;font-size:3px;line-height:8px;text-align:center">01</div>
  <div class="dot" style="left:58px;top:56px;width:8px;height:8px;background:var(--lime);color:#fff;font-size:3px;line-height:8px;text-align:center">02</div>
  <div class="dot" style="left:102px;top:56px;width:8px;height:8px;background:var(--navy);color:#fff;font-size:3px;line-height:8px;text-align:center">03</div>
  <div class="dot" style="left:146px;top:56px;width:8px;height:8px;background:var(--slate);color:#fff;font-size:3px;line-height:8px;text-align:center">04</div>
  <div class="copy" style="left:25px;top:58px"><b>Lorem Ipsum</b></div>
  <div class="copy" style="left:69px;top:58px"><b>Lorem Ipsum</b></div>
  <div class="copy" style="left:113px;top:58px"><b>Lorem Ipsum</b></div>
  <div class="copy" style="left:157px;top:58px"><b>Lorem Ipsum</b></div>
  <div class="copy" style="left:14px;top:68px;width:38px">Lorem ipsum dolor sit amet consectetuer elit sed diam nonummy</div>
  <div class="copy" style="left:58px;top:68px;width:38px">Lorem ipsum dolor sit amet consectetuer elit sed diam nonummy</div>
  <div class="copy" style="left:102px;top:68px;width:38px">Lorem ipsum dolor sit amet consectetuer elit sed diam nonummy</div>
  <div class="copy" style="left:146px;top:68px;width:38px">Lorem ipsum dolor sit amet consectetuer elit sed diam nonummy</div>
  <div class="footer">Ridgeway Schools Wellness Trust. All rights reserved.</div>
</section>

<section class="slide hub" style="left:503px;top:333px">
  <div class="title">Lorem Ipsum</div>
  <svg style="left:67px;top:20px" width="62" height="84" viewBox="0 0 62 84">
    <circle cx="31" cy="44" r="18" fill="#fff" stroke="#a9c6ea" stroke-width="2"/>
    <circle cx="31" cy="18" r="5" fill="var(--green)"/><circle cx="50" cy="26" r="5" fill="var(--navy)"/>
    <circle cx="56" cy="44" r="5" fill="var(--lime)"/><circle cx="50" cy="62" r="5" fill="var(--slate)"/>
    <circle cx="31" cy="70" r="5" fill="var(--green)"/><circle cx="12" cy="62" r="5" fill="var(--navy)"/>
    <circle cx="6" cy="44" r="5" fill="var(--lime)"/><circle cx="12" cy="26" r="5" fill="var(--slate)"/>
  </svg>
  <div class="copy" style="left:88px;top:62px;width:20px;text-align:center"><b>Lorem Ipsum</b></div>
  <div class="copy" style="left:14px;top:24px;width:50px;text-align:right"><b>Lorem Ipsum</b><br>Lorem ipsum dolor sit amet elit</div>
  <div class="copy" style="left:14px;top:42px;width:50px;text-align:right"><b>Lorem Ipsum</b><br>Lorem ipsum dolor sit amet elit</div>
  <div class="copy" style="left:14px;top:60px;width:50px;text-align:right"><b>Lorem Ipsum</b><br>Lorem ipsum dolor sit amet elit</div>
  <div class="copy" style="left:14px;top:78px;width:50px;text-align:right"><b>Lorem Ipsum</b><br>Lorem ipsum dolor sit amet elit</div>
  <div class="copy" style="left:132px;top:24px;width:50px"><b>Lorem Ipsum</b><br>Lorem ipsum dolor sit amet elit</div>
  <div class="copy" style="left:132px;top:42px;width:50px"><b>Lorem Ipsum</b><br>Lorem ipsum dolor sit amet elit</div>
  <div class="copy" style="left:132px;top:60px;width:50px"><b>Lorem Ipsum</b><br>Lorem ipsum dolor sit amet elit</div>
  <div class="copy" style="left:132px;top:78px;width:50px"><b>Lorem Ipsum</b><br>Lorem ipsum dolor sit amet elit</div>
  <div class="footer">Ridgeway Schools Wellness Trust. All rights reserved.</div>
</section>

<section class="slide cycle" style="left:713px;top:333px">
  <div class="title">Lorem Ipsum</div>
  <div style="left:0;top:60px;width:100px;height:7px;background:var(--slate);color:#fff;font-size:2.6px;line-height:7px;padding-left:30px;font-weight:700">Lorem ipsum dolor sit amet</div>
  <div style="left:98px;top:54px;width:97px;height:7px;background:var(--lime);color:#fff;font-size:2.6px;line-height:7px;padding-left:6px;font-weight:700">Lorem ipsum dolor sit amet</div>
  <svg style="left:74px;top:30px" width="52" height="58" viewBox="0 0 52 58">
    <path d="M8 22 A19 19 0 0 1 44 18" fill="none" stroke="var(--slate)" stroke-width="6"/>
    <path d="M44 18 l5 -8 l2 11 z" fill="var(--slate)"/>
    <path d="M46 34 A19 19 0 0 1 8 40" fill="none" stroke="var(--lime)" stroke-width="6"/>
    <path d="M8 40 l-5 8 l-2 -11 z" fill="var(--lime)"/>
    <circle cx="26" cy="29" r="4" fill="var(--green)"/>
  </svg>
  <div style="left:22px;top:30px;width:20px;height:26px;background:var(--navy);border-radius:2px"></div>
  <div class="copy box-label" style="left:23px;top:32px;width:18px"><b>Lorem Ipsum</b> dolor sit amet elit</div>
  <div style="left:46px;top:30px;width:20px;height:26px;background:var(--navy);border-radius:2px"></div>
  <div class="copy box-label" style="left:47px;top:32px;width:18px"><b>Lorem Ipsum</b> dolor sit amet elit</div>
  <div style="left:133px;top:66px;width:20px;height:26px;background:var(--green);border-radius:2px"></div>
  <div class="copy box-label" style="left:134px;top:68px;width:18px"><b>Lorem Ipsum</b> dolor sit amet elit</div>
  <div style="left:156px;top:66px;width:20px;height:26px;background:var(--green);border-radius:2px"></div>
  <div class="copy box-label" style="left:157px;top:68px;width:18px"><b>Lorem Ipsum</b> dolor sit amet elit</div>
  <div class="footer">Ridgeway Schools Wellness Trust. All rights reserved.</div>
</section>

<section class="slide world" style="left:923px;top:333px">
  <div class="title">Lorem Ipsum</div>
  <div class="copy wide" style="top:18px">Lorem ipsum dolor sit amet, consectetuer adipiscing elit, sed diam nonummy nibh euismod tincidunt ut laoreet dolore magna aliquam erat volutpat ut wisi enim ad minim veniam.</div>
  <div role="img" aria-label="World map with location markers" style="left:60px;top:42px;width:80px;height:48px;border-radius:18px;background:linear-gradient(135deg,#d6d6d6,#bfbfbf)"></div>
  <div class="copy" style="left:32px;top:58px"><b>Lorem Ipsum</b></div>
  <div class="copy" style="left:145px;top:50px"><b style="color:var(--green)">Lorem Ipsum</b></div>
  <div class="copy" style="left:60px;top:92px"><b>Lorem Ipsum</b></div>
  <div class="copy" style="left:124px;top:92px"><b>Lorem Ipsum</b></div>
  <div class="footer">Ridgeway Schools Wellness Trust. All rights reserved.</div>
</section>

<!-- Row 4 -->
<section class="slide gantt" style="left:83px;top:454px">
  <div class="title">Lorem Ipsum</div>
  <svg style="left:76px;top:20px" width="20" height="20" viewBox="0 0 20 20"><circle cx="10" cy="10" r="9" fill="var(--mint)"/><path d="M10 10 L10 1 A9 9 0 1 1 3 16 Z" fill="var(--green)"/></svg>
  <svg style="left:110px;top:20px" width="20" height="20" viewBox="0 0 20 20"><circle cx="10" cy="10" r="9" fill="var(--ice)"/><path d="M10 10 L10 1 A9 9 0 1 1 1 11 Z" fill="var(--slate)"/></svg>
  <div class="copy" style="left:46px;top:22px;width:28px;text-align:right">Lorem ipsum dolor sit amet</div>
  <div class="copy" style="left:132px;top:22px;width:40px">Lorem ipsum dolor sit amet consectetuer</div>
  <div style="left:14px;top:46px;width:170px;height:5px;background:var(--ice)"></div><div style="left:14px;top:46px;width:30px;height:5px;background:var(--green)"></div><div style="left:150px;top:46px;width:34px;height:5px;background:var(--slate)"></div>
  <div style="left:14px;top:54px;width:170px;height:5px;background:var(--mint)"></div><div style="left:86px;top:54px;width:36px;height:5px;background:var(--lime)"></div>
  <div style="left:14px;top:62px;width:170px;height:5px;background:var(--ice)"></div><div style="left:14px;top:62px;width:40px;height:5px;background:var(--green)"></div><div style="left:140px;top:62px;width:44px;height:5px;background:var(--navy)"></div>
  <div style="left:14px;top:70px;width:170px;height:5px;background:var(--mint)"></div><div style="left:14px;top:70px;width:54px;height:5px;background:var(--green)"></div><div style="left:86px;top:70px;width:36px;height:5px;background:var(--lime)"></div>
  <div style="left:14px;top:78px;width:170px;height:5px;background:var(--ice)"></div><div style="left:14px;top:78px;width:36px;height:5px;background:var(--green)"></div><div style="left:144px;top:78px;width:40px;height:5px;background:var(--slate)"></div>
  <div style="left:14px;top:86px;width:170px;height:5px;background:var(--mint)"></div><div style="left:86px;top:86px;width:36px;height:5px;background:var(--slate)"></div>
  <div class="footer">Ridgeway Schools Wellness Trust. All rights reserved.</div>
</section>

<section class="slide shapes" style="left:293px;top:454px">
  <div class="title">Infographic Style</div>
  <div class="para" style="left:0;top:40px;width:30px;background:var(--green)"></div>
  <div class="para" style="left:36px;top:40px;width:40px;background:var(--lime)">Lorem Ipsum<br>dolor sit amet</div>
  <div class="para" style="left:82px;top:40px;width:40px;background:var(--navy)">Lorem Ipsum<br>dolor sit amet</div>
  <div class="para" style="left:128px;top:40px;width:40px;background:var(--slate)">Lorem Ipsum<br>dolor sit amet</div>
  <div class="para" style="left:20px;top:57px;width:40px;background:var(--slate)">Lorem Ipsum<br>dolor sit amet</div>
  <div class="para" style="left:66px;top:57px;width:40px;background:var(--navy)">Lorem Ipsum<br>dolor sit amet</div>
  <div class="para" style="left:112px;top:57px;width:40px;background:var(--lime)">Lorem Ipsum<br>dolor sit amet</div>
  <div class="para" style="left:158px;top:57px;width:40px;background:var(--green)"></div>
  <div class="footer">Ridgeway Schools Wellness Trust. All rights reserved.</div>
</section>

<section class="slide donuts" style="left:503px;top:454px">
  <div class="title">Infographic Style</div>
  <svg style="left:14px;top:26px" width="180" height="72" viewBox="0 0 180 72">
    <g fill="none" stroke-width="3.5">
      <circle cx="20" cy="16" r="10" stroke="#e4e4e4"/><circle cx="20" cy="16" r="10" stroke="var(--green)" stroke-dasharray="34 63" transform="rotate(-90 20 16)"/>
      <circle cx="90" cy="16" r="10" stroke="#e4e4e4"/><circle cx="90" cy="16" r="10" stroke="var(--slate)" stroke-dasharray="38 63" transform="rotate(-90 90 16)"/>
      <circle cx="160" cy="16" r="10" stroke="#e4e4e4"/><circle cx="160" cy="16" r="10" stroke="var(--navy)" stroke-dasharray="40 63" transform="rotate(-90 160 16)"/>
      <circle cx="62" cy="52" r="10" stroke="#e4e4e4"/><circle cx="62" cy="52" r="10" stroke="var(--lime)" stroke-dasharray="36 63" transform="rotate(-90 62 52)"/>
      <circle cx="132" cy="52" r="10" stroke="#e4e4e4"/><circle cx="132" cy="52" r="10" stroke="#a9c6ea" stroke-dasharray="38 63" transform="rotate(-90 132 52)"/>
    </g>
    <g font-family="Arimo, Arial, sans-serif" font-size="4" fill="var(--ink)" text-anchor="middle">
      <text x="20" y="18">55%</text><text x="90" y="18">60%</text><text x="160" y="18">63%</text><text x="62" y="54">58%</text><text x="132" y="54">60%</text>
    </g>
  </svg>
  <div class="copy" style="left:51px;top:37px;width:28px">Lorem ipsum dolor sit amet elit</div>
  <div class="copy" style="left:118px;top:37px;width:28px">Lorem ipsum dolor sit amet elit</div>
  <div class="copy" style="left:31px;top:73px;width:28px;text-align:right">Lorem ipsum dolor sit amet elit</div>
  <div class="copy" style="left:162px;top:73px;width:28px">Lorem ipsum dolor sit amet elit</div>
  <div class="footer">Ridgeway Schools Wellness Trust. All rights reserved.</div>
</section>

</div>
</body>
</html>
```